Maltrey Pools & Patio Homepage Design

I am looking for someone to design a one-page website for a company called Maltrey Pools & Patio. While the content will be different, the design should be similar to https://maltrey-example.com/pools-patio/.
Industry/Entity Type
Pool Cleaning Service
Number of Pages Required
1 page
Font styles to use
- See brand guidelines

Requirements
Must have
- Must be similar in style https://maltrey-example.com/pools-patio/. Look at the Word Doc for the content.

```html
<!DOCTYPE html>
<html lang="en">
<head>
<meta charset="utf-8">
<title>Maltrey Pools &amp; Patio</title>
<link rel="stylesheet" href="https://fonts.googleapis.com/css2?family=Barlow+Condensed:wght@400;600;700&family=Roboto:wght@300;400;500&family=Montserrat:wght@400;600&display=swap">
<style>
:root{
  --blue:#1f8ad6;
  --blue-dark:#1470b8;
  --green:#63c51f;
  --green-light:#7bd332;
  --ink:#222;
  --muted:#555;
  --paper:#f4f4f4;
  --footer:#141414;
  --white:#fff;
}
*{box-sizing:border-box;margin:0;padding:0}
html,body{width:1200px;height:4310px;overflow:hidden}
body{font-family:"Roboto",sans-serif;color:var(--ink);background:var(--white);position:relative}
.cond{font-family:"Barlow Condensed",sans-serif}
section,header,footer{position:absolute;left:0;width:1200px}

/* header */
.site-header{top:0;height:78px;background:var(--blue)}
.site-header .brand-zone{position:absolute;left:0;top:0;width:365px;height:78px;background:var(--white);clip-path:polygon(0 0,100% 0,88% 100%,0 100%)}
.brand{position:absolute;left:100px;top:18px;display:flex;align-items:center;gap:10px;font-family:"Roboto",sans-serif;font-weight:500;font-size:36px;color:var(--blue);line-height:1}
.brand .dot{width:34px;height:34px;border-radius:50%;background:var(--green)}
.nav{position:absolute;left:384px;top:0;height:78px;display:flex;align-items:center;gap:38px;font-family:"Barlow Condensed",sans-serif;font-weight:700;font-size:18px;color:var(--white)}
.nav .phone{display:flex;align-items:center;gap:10px;margin-left:-10px}
.nav .phone i{width:44px;height:44px;border-radius:50%;background:var(--green);display:flex;align-items:center;justify-content:center;border:2px solid rgba(255,255,255,.6)}

/* hero */
.hero{top:78px;height:533px}
.hero .photo{position:absolute;inset:0;background:linear-gradient(160deg,#5f8f7c 0%,#3c7fae 35%,#2a8fd0 60%,#4bb0e0 80%,#3a7a52 100%)}
.hero .photo::after{content:"";position:absolute;inset:0;background:rgba(20,110,190,.35)}
.hero h1{position:absolute;left:100px;top:122px;font-family:"Barlow Condensed",sans-serif;font-weight:700;font-size:60px;line-height:70px;color:var(--white);text-transform:uppercase;z-index:2}
.book-card{position:absolute;left:748px;top:57px;width:352px;height:424px;background:var(--white);border-radius:6px;padding:20px;z-index:2}
.book-card h2{font-family:"Barlow Condensed",sans-serif;font-weight:700;font-size:23px;color:var(--blue);margin-bottom:14px}
.field{border:2px solid var(--green);border-radius:5px;height:38px;font-size:11px;color:#666;padding:11px 8px}
.grid2{display:grid;grid-template-columns:1fr 1fr;gap:16px}
.book-card .grid2{margin-bottom:16px}
.book-card .area{height:72px;margin-bottom:14px}
.book-card h3{font-family:"Barlow Condensed",sans-serif;font-weight:600;font-size:17px;margin:0 0 8px 6px}
.radios{display:flex;gap:26px;margin-left:10px;font-size:15px;color:#333}
.radios span::before{content:"";display:inline-block;width:9px;height:9px;border-radius:50%;background:var(--blue);margin-right:8px}
.btn{position:absolute;display:block;height:52px;font-family:"Barlow Condensed",sans-serif;font-weight:700;font-size:19px;text-align:center;line-height:52px}
.btn .back{position:absolute;inset:0;clip-path:polygon(12% 0,100% 0,88% 100%,0 100%)}
.btn .front{position:absolute;left:16px;right:0;top:0;bottom:0;clip-path:polygon(0 0,100% 0,88% 100%,0 100%)}
.btn .label{position:relative}
.btn-green .back{background:var(--blue)}
.btn-green .front{background:var(--green)}
.btn-green{color:var(--white)}

/* about */
.about{top:611px;height:733px;background:linear-gradient(180deg,#fff 0%,#fff 45%,#e9f3f7 62%,#5bc6dc 78%,#3eb4d6 90%,#8d8b82 100%)}
.about .pic{position:absolute;left:132px;top:110px;width:395px;height:440px;background:linear-gradient(180deg,#b7c7d8 0%,#8d6f56 45%,#4aaed0 75%,#2f99c4 100%);border-radius:24px}
.about .accent{position:absolute;background:var(--green)}
.about .accent.a{left:188px;top:115px;width:44px;height:80px;clip-path:polygon(50% 0,100% 25%,100% 75%,0 100%,0 25%)}
.about .accent.b{left:62px;top:230px;width:90px;height:70px;clip-path:polygon(100% 0,100% 40%,0 100%,0 75%)}
.mark{width:26px;height:26px;border-radius:50%;border:3px solid var(--green)}
.about .mark{position:absolute;left:628px;top:68px}
.about .eyebrow{position:absolute;left:620px;top:108px;font-family:"Barlow Condensed",sans-serif;font-weight:700;font-size:32px;color:var(--blue)}
.about .big{position:absolute;left:620px;top:148px;font-family:"Barlow Condensed",sans-serif;font-weight:700;font-size:76px;color:var(--blue);letter-spacing:1px}
.about .copy{position:absolute;left:630px;top:250px;width:475px;font-size:12.5px;line-height:21.5px;color:#666}
.about .copy p{margin-bottom:16px}

/* services */
.services{top:1344px;height:593px}
.section-title{position:absolute;left:0;width:1200px;text-align:center;font-family:"Barlow Condensed",sans-serif;font-weight:700;font-size:44px}
.section-mark{position:absolute;left:587px}
.services .section-mark{top:80px}
.services .section-title{top:112px;color:var(--blue)}
.svc{position:absolute;top:197px;width:320px}
.svc .img{height:190px;border-radius:3px}
.svc h3{font-family:"Barlow Condensed",sans-serif;font-weight:700;font-size:29px;color:var(--blue);margin:16px 0 10px 4px}
.svc p{font-size:14px;line-height:21.5px;color:#444;margin-left:4px;width:300px}

/* testimonial */
.testimonial{top:1937px;height:493px;background:radial-gradient(ellipse at 30% 40%,#8ede48 0%,#6bcb28 50%,#5ab81d 100%)}
.testimonial h2{position:absolute;left:100px;top:106px;font-family:"Barlow Condensed",sans-serif;font-weight:700;font-size:48px;color:var(--white)}
.testimonial p{position:absolute;left:100px;top:186px;width:560px;font-weight:300;font-size:19px;line-height:33px;color:var(--white)}
.btn-blue{color:var(--white)}
.btn-blue .back{background:var(--white)}
.btn-blue .front{background:var(--blue)}
.ring{position:absolute;left:728px;top:60px;width:380px;height:380px;border-radius:50%;background:var(--blue)}
.portrait{position:absolute;left:755px;top:87px;width:326px;height:326px;border-radius:50%;background:radial-gradient(circle at 50% 40%,#d9b49a 0%,#b98d72 35%,#4d5560 70%,#2d333b 100%)}

/* service area */
.area-sec{top:2430px;height:577px;background:var(--paper)}
.area-sec .section-mark{top:72px}
.area-sec .section-title{top:102px;color:#111}
.town{position:absolute;top:196px;width:238px;text-align:center}
.town .img{height:249px;border-radius:3px}
.town h3{font-family:"Barlow Condensed",sans-serif;font-weight:600;font-size:29px;color:#111;margin-top:16px}

/* contact */
.contact{top:3007px;height:885px;background:linear-gradient(135deg,#2a8fe0 0%,#1f82d4 50%,#2a8cdc 100%);color:var(--white)}
.contact .section-mark{top:57px;border-color:var(--white)}
.contact .section-title{top:90px}
.contact .lead{position:absolute;left:140px;top:170px;width:920px;text-align:center;font-family:"Barlow Condensed",sans-serif;font-size:21px;line-height:34px}
.contact .call{position:absolute;left:0;top:280px;width:1200px;text-align:center;font-family:"Barlow Condensed",sans-serif;font-weight:700;font-size:28px}
.cform{position:absolute;left:155px;top:363px;width:855px}
.cform .field{background:var(--white);border:none;height:47px;font-size:16px;color:#444;padding:15px 16px;font-family:"Barlow Condensed",sans-serif}
.cform .grid2{gap:24px;margin-bottom:17px}
.cform h3{font-family:"Barlow Condensed",sans-serif;font-weight:400;font-size:27px;margin:28px 0 10px 14px}
.cform ul{list-style:none;margin-left:14px;font-family:"Barlow Condensed",sans-serif;font-size:26px;line-height:38px}
.cform li::before{content:"";display:inline-block;width:14px;height:14px;border-radius:50%;background:var(--green);margin-right:14px;vertical-align:2px}
.btn-white{color:var(--blue)}
.btn-white .back{background:var(--green)}
.btn-white .front{background:var(--white)}

/* footer */
.site-footer{top:3892px;height:418px;background:var(--footer);color:var(--white);font-family:"Montserrat",sans-serif}
.site-footer .brand{left:100px;top:100px;color:var(--blue);font-size:40px}
.social{position:absolute;left:115px;top:260px;display:flex;gap:8px}
.social span{width:30px;height:30px;border-radius:50%;border:1.5px solid #ccc}
.fcol{position:absolute;top:55px;font-size:13px;line-height:20px}
.fcol h4{font-size:17px;font-weight:600;margin-bottom:16px}
.fcol li{list-style:none;margin-bottom:10px}
.fcol .lab{margin-top:12px}
.news{position:absolute;left:810px;top:165px;width:276px;height:38px;border-radius:19px;background:var(--white);color:#333;font-size:11px;padding:12px 20px}
.news i{position:absolute;right:14px;top:10px;width:18px;height:18px;border-radius:50%;background:#111}
.site-footer hr{position:absolute;left:110px;top:326px;width:980px;border:none;border-top:1px solid #555}
.copyright{position:absolute;top:350px;width:1200px;text-align:center;font-size:14px}
</style>
</head>
<body>

<header class="site-header">
  <div class="brand-zone"></div>
  <div class="brand"><span class="dot"></span>maltrey</div>
  <nav class="nav">
    <span>Home</span><span>About Us</span><span>Services</span><span>Technician</span><span>Contact Us</span>
    <span class="phone"><i><svg width="20" height="20" viewBox="0 0 24 24"><path fill="#fff" d="M6.6 10.8a15.1 15.1 0 0 0 6.6 6.6l2.2-2.2c.3-.3.7-.4 1-.2 1.1.4 2.3.6 3.6.6.6 0 1 .4 1 1V20c0 .6-.4 1-1 1A17 17 0 0 1 3 4c0-.6.4-1 1-1h3.5c.6 0 1 .4 1 1 0 1.3.2 2.5.6 3.6.1.3 0 .7-.2 1z"/></svg></i>+1 555.014.2290</span>
  </nav>
</header>

<section class="hero">
  <div class="photo" role="img" aria-label="Sunlit backyard pool with lounge chairs and tropical plants"></div>
  <h1>Keep your pool<br>sparkling with<br>Maltrey!</h1>
  <form class="book-card">
    <h2>BOOK AN APPOINTMENT</h2>
    <div class="grid2"><div class="field">First Name</div><div class="field">Last Name</div></div>
    <div class="grid2"><div class="field">Phone</div><div class="field">Email</div></div>
    <div class="field area">Address</div>
    <h3>Preferred Contact Method</h3>
    <div class="radios"><span>Call</span><span>Text</span><span>Email</span></div>
    <span class="btn btn-green" style="left:22px;top:347px;width:205px"><span class="back"></span><span class="front"></span><span class="label">BOOK NOW</span></span>
  </form>
</section>

<section class="about">
  <div class="accent a"></div>
  <div class="accent b"></div>
  <div class="pic" role="img" aria-label="Technician cleaning a backyard pool with a pole in front of a house"></div>
  <div class="mark"></div>
  <div class="eyebrow">ABOUT US</div>
  <div class="big">MALTREY</div>
  <div class="copy">
    <p>We're Maltrey Pools &amp; Patio, and we specialize in pool cleaning and repair services that will keep your pool looking its best. Our reliable and professional team is committed to helping you get the most out of your backyard oasis, ensuring it's always ready for all types of fun when you want it. Our weekly pool cleaning service is affordable and ensures that your pool is properly taken care of throughout the swimming season.</p>
    <p>When you choose us as your go-to for all things pools, relaxing days spent on a clean lounge chair are worry-free because we take care of all the hard work! From chemical balancing to scrubbing and filter maintenance - there's nothing too big or small for us.</p>
  </div>
  <span class="btn btn-green" style="left:630px;top:487px;width:205px"><span class="back"></span><span class="front"></span><span class="label">BOOK NOW</span></span>
</section>

<section class="services">
  <div class="mark section-mark"></div>
  <h2 class="section-title">OUR SERVICES</h2>
  <article class="svc" style="left:98px">
    <div class="img" role="img" aria-label="Pool skimmer net holding autumn leaves over blue water" style="background:linear-gradient(135deg,#36b6e8,#1b7fd0 55%,#e07b2a 70%,#2aa4e0)"></div>
    <h3>Pool Cleaning</h3>
    <p>Our weekly service includes chemical balancing, debris removal, wall and step scrubbing, and filter maintenance. Standard chemicals are included in the quoted price.</p>
  </article>
  <article class="svc" style="left:440px">
    <div class="img" role="img" aria-label="Robotic pool cleaner on a tiled pool floor" style="background:linear-gradient(135deg,#6fc7ea,#2e9fd6 50%,#d9e4ea 65%,#3aa7d9)"></div>
    <h3>Pool Maintenance</h3>
    <p>We perform regular checks on all your pool equipment to make sure it runs efficiently and safely.</p>
  </article>
  <article class="svc" style="left:781px">
    <div class="img" role="img" aria-label="Pool vacuum hose coiled at the edge of a pool" style="background:linear-gradient(180deg,#a9a7a2,#6d8b96 45%,#2c7da6 75%,#1f6690)"></div>
    <h3>Pool Repair</h3>
    <p>From plumbing to equipment malfunctions, our qualified technicians can diagnose and repair any pool problem you may have.</p>
  </article>
</section>

<section class="testimonial">
  <h2>DALE HARMON</h2>
  <p>"I understand that keeping your pool clean and well-maintained is a priority for you, which is why I'm committed to providing top-notch pool cleaning and repair services.</p>
  <span class="btn btn-blue" style="left:104px;top:331px;width:262px"><span class="back"></span><span class="front"></span><span class="label">LET'S GET STARTED!</span></span>
  <div class="ring"></div>
  <div class="portrait" role="img" aria-label="Portrait of the pool technician"></div>
</section>

<section class="area-sec">
  <div class="mark section-mark"></div>
  <h2 class="section-title">SERVICE AREA</h2>
  <div class="town" style="left:98px"><div class="img" role="img" aria-label="Aerial view of a boat on a lake by an orange shoreline" style="background:linear-gradient(100deg,#c9862c 0%,#b6702a 30%,#1f8a8e 45%,#167f8a 100%)"></div><h3>Argyle</h3></div>
  <div class="town" style="left:352px"><div class="img" role="img" aria-label="Boat moving through a narrow canal between cliffs" style="background:linear-gradient(90deg,#9c8468 0%,#b39a7a 30%,#2ea3b8 45%,#2ea3b8 55%,#9a7d5f 70%,#6fa0c8 100%)"></div><h3>Corinth</h3></div>
  <div class="town" style="left:607px"><div class="img" role="img" aria-label="Aerial view of a canal lined with houses and trees" style="background:linear-gradient(120deg,#b5a48f 0%,#7c8a62 35%,#8fa58a 55%,#6a7e4d 75%,#c2b6a2 100%)"></div><h3>Flower Mound</h3></div>
  <div class="town" style="left:861px"><div class="img" role="img" aria-label="Motorboat on a wide blue lake under a clear sky" style="background:linear-gradient(180deg,#5a86d6 0%,#7aa4e4 45%,#2d56a8 55%,#1f4a9a 100%)"></div><h3>Lewisville</h3></div>
</section>

<section class="contact">
  <div class="mark section-mark"></div>
  <h2 class="section-title">CONTACT US</h2>
  <p class="lead">Contact us today at Maltrey Pools &amp; Patio, and let's discuss how our professionals can help bridge the gap between what your pool could be and what it actually is! Get ready to have a worry-free experience with quality service delivered right on time so you can start enjoying those waves anytime soon!</p>
  <div class="call">Give us a call today at 555-014-2291</div>
  <form class="cform">
    <div class="grid2"><div class="field">First Name</div><div class="field">Last Name</div></div>
    <div class="grid2"><div class="field">Phone</div><div class="field">Email</div></div>
    <div class="field">Address</div>
    <h3>Preferred Contact Method</h3>
    <ul><li>Call</li><li>Text</li><li>Email</li></ul>
  </form>
  <span class="btn btn-white" style="left:173px;top:770px;width:205px"><span class="back"></span><span class="front"></span><span class="label">BOOK NOW</span></span>
</section>

<footer class="site-footer">
  <div class="brand"><span class="dot"></span>maltrey</div>
  <div class="social"><span></span><span></span><span></span></div>
  <div class="fcol" style="left:363px">
    <h4>More Info</h4>
    <ul><li>Terms &amp; Conditions</li><li>Privacy Policy</li><li>About Us</li><li>Support</li></ul>
  </div>
  <div class="fcol" style="left:561px;width:180px">
    <h4>Contact Us</h4>
    <div>ADDRESS</div>
    <div>&#9679; Lorem ipsum dolor sit amet, consectetur</div>
    <div class="lab">PHONE</div>
    <div>&#9742; +1 888-888-8888</div>
    <div class="lab">EMAIL</div>
    <div>&#9993; info@maltrey-example.com</div>
  </div>
  <div class="fcol" style="left:812px;width:270px">
    <h4>Newsletter</h4>
    <div>Lorem ipsum dolor sit amet, consectetur adipiscing elit, sed do eiusmod tempor</div>
  </div>
  <div class="news">Enter Email<i></i></div>
  <hr>
  <div class="copyright">© copyrights 2023 Maltrey &nbsp;|&nbsp; All Rights Reserved</div>
</footer>

</body>
</html>
```